Business card for Drone Aerial

I need a business card designed keeping in mind I want to do post cards also with a similar design.
Both sides of the card would be cool.
I have a vortel 8 max and would like a picture of it on the front of the card. Similar to one I attached.
I really like the look of a drone in the air and the background pic a little blurry. I attached a few images as IDEAS.
Some special things I want to be on the card additional to the normal business card info:
"Aerial Photography" or "Hover Frame Aerial Photography"?
"KTO# 58203917"

I like modern and creative. My Favorite color is blue and I like blue on white.
I do not have a business name and am not going to have one. When they read "Aerial Photography" and see the drone and image they will know what the card is for.

FYI, The attached pictures are just images from pixelgrove and just samples/ideas.

Target Market(s)

Real estate, construction, events

Industry/Entity Type

Business

Contact Information for Business Card

Also Definitely want to contain, my name, my number and email address.

Requirements
Must have
• "KTO# 58203917"
• "Aerial Photography"

```html
<!DOCTYPE html>
<html lang="en">
<head>
<meta charset="utf-8">
<title>Hover Frame Aerial Photography – Business Card</title>
<link rel="stylesheet" href="https://fonts.googleapis.com/css2?family=Montserrat:wght@400;500;600&display=swap">
<style>
  :root {
    --page-bg: #e9eaec;
    --card-white: #ffffff;
    --brand-blue: #1677d6;
    --deep-blue: #0f5fb3;
    --navy-ink: #15263d;
    --ink: #1c1f24;
    --logo-light: #e6e8ec;
    --drone-soft: #eef1f5;
    --drone-accent: #d9e4f2;
  }
  * { margin: 0; padding: 0; box-sizing: border-box; }
  html, body {
    width: 1200px; height: 1021px; overflow: hidden;
    background: var(--page-bg);
    font-family: "Montserrat", sans-serif;
  }
  .sheet {
    position: relative; width: 1200px; height: 1021px;
  }
  .card {
    position: absolute; left: 220px; width: 760px; height: 434px;
    box-shadow: 0 6px 18px rgba(0,0,0,0.12);
    overflow: hidden;
  }
  .card--front { top: 50px; background: var(--card-white); }
  .card--back { top: 537px; background: var(--brand-blue); }

  .wordmark { position: absolute; }
  .wordmark__name {
    display: block; font-weight: 600; letter-spacing: 0.5px; line-height: 1;
  }
  .wordmark__tagline {
    display: block; font-weight: 500; letter-spacing: 5px; text-transform: uppercase;
    margin-top: 8px;
  }

  .card--front .wordmark { left: 62px; top: 112px; }
  .card--front .wordmark__name { font-size: 38px; color: var(--brand-blue); }
  .card--front .wordmark__tagline { font-size: 11px; color: var(--ink); }

  .drone-visual {
    position: absolute; right: 56px; top: 40px; width: 300px; height: 250px;
    border-radius: 18px;
    background: radial-gradient(ellipse at 50% 50%, var(--drone-accent) 0%, var(--drone-soft) 45%, var(--card-white) 75%);
  }

  .contact {
    position: absolute; left: 62px; bottom: 58px;
    list-style: none; font-size: 15px; color: var(--ink);
  }
  .contact__item { display: flex; align-items: center; gap: 10px; margin-top: 10px; }
  .contact__icon { width: 16px; height: 16px; fill: var(--deep-blue); flex: none; }
  .contact__item--license { color: var(--brand-blue); font-size: 15px; }

  .card--back .wordmark {
    left: 0; right: 0; top: 168px; text-align: center;
  }
  .card--back .wordmark__name { font-size: 54px; color: var(--logo-light); }
  .card--back .wordmark__tagline {
    font-size: 15px; color: var(--navy-ink); letter-spacing: 7px; margin-top: 12px;
  }
</style>
</head>
<body>
<main class="sheet">
  <section class="card card--front" aria-label="Card front">
    <div class="wordmark">
      <span class="wordmark__name">Hover Frame</span>
      <span class="wordmark__tagline">Aerial Photography</span>
    </div>

    <div class="drone-visual" role="img" aria-label="Faint photo of a white vortel 8 max quadcopter drone with camera gimbal"></div>

    <ul class="contact">
      <li class="contact__item">
        <svg class="contact__icon" viewBox="0 0 16 16" aria-hidden="true">
          <path d="M1 5c0-2 3-3 7-3s7 1 7 3v1.5h-3.5V5h-7v1.5H1z"/>
          <path d="M4 7h8l2 6H2z"/>
        </svg>
        <span>000 000 0000</span>
      </li>
      <li class="contact__item">
        <svg class="contact__icon" viewBox="0 0 16 16" aria-hidden="true">
          <path d="M1 3h14v10H1z M2 4l6 5 6-5" fill="none" stroke="currentColor"/>
          <rect x="1" y="3" width="14" height="10"/>
          <path d="M1.5 3.5 8 9l6.5-5.5" fill="none" stroke="#fff" stroke-width="1.4"/>
        </svg>
        <span>mail@hoverframe.net</span>
      </li>
      <li class="contact__item contact__item--license">
        <span>KTO# 58203917</span>
      </li>
    </ul>
  </section>

  <section class="card card--back" aria-label="Card back">
    <div class="wordmark">
      <span class="wordmark__name">Hover Frame</span>
      <span class="wordmark__tagline">Aerial Photography</span>
    </div>
  </section>
</main>
</body>
</html>
```